Postcard double sided

Title: DWIGHT'S REVENGE

Why would Dwight Kessler align himself with Gordon Pruett?

(photo of two guys)

Dwight approached elected officials that he wanted to run for office, but did not have money to finance his campaign. He wanted other elected officials to finance his campaign. Everyone told him that they would help him get the vote out, but that he needed to finance his own race.

In comes Gordon Pruett.

Gordon Pruett who has a pay to play scheme over at the City, told Dwight he would finance his campaign on one condition.

He needed to run against Steven Hulse.

Why would Dwight want to run with no money?

Backside

DWIGHT'S REVENGE

Dwight decided to run because no one on the school board would terminate Dwight's ex and her new boyfriend who both work for the school district. His ex even filed criminal charges against him that are still pending.

Mug Shot facing left (name the charges Criminal Trespass , and Criminal Mischief (highlight bold letters use two lines) mug shot facing right

Complaint one (then photo with full face) Compliant 2)
(showcharges)

Dwight's ultimate goal is to terminate his ex and her new boyfriend if elected.
Plus Gordon Pruett needs the majority on the school board to do what he does bet.

Kickbacks for Contracts.

They will hire their own contractors!
Say "No" to Dwight's Revenge and Gordon Pruett Money Grab!

Title On Back: all caps: DOMESTIC VIOLENCE

```html
<!DOCTYPE html>
<html lang="en">
<head>
<meta charset="utf-8">
<title>Dwight's Revenge – Postcard</title>
<link href="https://fonts.googleapis.com/css2?family=Oswald:wght@700&family=Tinos:wght@400;700&display=swap" rel="stylesheet">
<style>
  :root {
    --red: #a0000f;
    --ink: #1b1a1e;
    --white: #ffffff;
    --backdrop: #000000;
    --rule: #555555;
    --paper: #f1f1f1;
  }
  * { box-sizing: border-box; margin: 0; padding: 0; }
  html, body { width: 848px; height: 1200px; overflow: hidden; background: var(--backdrop); }
  body { position: relative; font-family: "Tinos", "Times New Roman", serif; color: var(--ink); }

  .card { position: absolute; left: 27px; width: 790px; height: 553px; background: var(--white); overflow: hidden; }
  .card--front { top: 30px; }
  .card--back { top: 612px; }
  .card svg.shapes { position: absolute; inset: 0; }
  .abs { position: absolute; }

  .front-title { left: 148px; width: 616px; top: 22px; text-align: center; font-family: "Oswald", "Arial Narrow", sans-serif; font-weight: 700; font-size: 42px; line-height: 1.2; color: var(--white); letter-spacing: 0.5px; }
  .front-question { left: 148px; width: 616px; top: 84px; text-align: center; font-size: 21px; line-height: 27px; color: var(--white); }
  .front-story { left: 29px; top: 330px; width: 320px; font-size: 16px; line-height: 22.5px; color: var(--white); }

  .right-block { right: 20px; text-align: right; }
  .kicker { font-weight: 700; font-size: 22px; line-height: 28px; color: var(--red); }
  .kicker-name { font-weight: 700; font-size: 22px; line-height: 28px; color: var(--ink); letter-spacing: 0.3px; }
  .intro-heading { top: 292px; }
  .intro-text { top: 358px; width: 340px; font-size: 16px; line-height: 23.5px; }
  .condition-heading { top: 443px; right: 37px; }
  .closing-question { top: 508px; right: 43px; font-size: 16px; line-height: 22px; }

  .back-title { left: 41px; top: 24px; font-family: "Oswald", "Arial Narrow", sans-serif; font-weight: 700; font-size: 44px; line-height: 1.2; letter-spacing: 0.3px; }
  .back-title .accent { color: var(--red); }
  .back-text { left: 42px; font-size: 15px; line-height: 20.5px; }
  .back-text--reason { top: 98px; width: 300px; }
  .back-text--goal { top: 213px; width: 180px; }
  .back-text--majority { top: 289px; width: 220px; }
  .kickbacks { left: 42px; top: 360px; font-weight: 700; font-size: 19.5px; line-height: 26px; }
  .kickbacks .accent { color: var(--red); }
  .back-text--contractors { top: 395px; }
  .slogan { left: 42px; top: 429px; font-weight: 700; font-size: 17px; line-height: 23px; }
  .slogan .accent { color: var(--red); }

  .charge { left: 336px; width: 100px; text-align: center; font-weight: 700; font-size: 14px; line-height: 16.5px; }
  .charge .accent { color: var(--red); }
  .charge--trespass { top: 205px; }
  .charge--mischief { top: 352px; }

  .stamp-box { left: 663px; top: 40px; width: 92px; height: 92px; border: 1px solid var(--rule); }
  .address-line { left: 497px; width: 284px; height: 0; border-top: 1px dashed var(--rule); }
</style>
</head>
<body>

<section class="card card--front">
  <svg class="shapes" viewBox="0 0 790 553" width="790" height="553" aria-hidden="false">
    <defs>
      <linearGradient id="duo-tone" x1="0" y1="0" x2="0" y2="1">
        <stop offset="0" stop-color="#f4f1ee"/>
        <stop offset="0.5" stop-color="#c9b3a3"/>
        <stop offset="1" stop-color="#3a3d46"/>
      </linearGradient>
    </defs>
    <polygon fill="var(--red)" points="0,0 132,0 469,274 777,0 790,0 790,67 198,553 0,553"/>
    <polygon fill="var(--ink)" points="148,0 764,0 469,263"/>
    <polygon fill="var(--white)" points="98,49 255,49 331,182 255,319 98,319 21,182"/>
    <polygon fill="url(#duo-tone)" role="img" aria-label="Photo of Dwight Kessler and Gordon Pruett standing together in suits" points="103,57 250,57 322,182 250,311 103,311 30,182"/>
  </svg>

  <h1 class="abs front-title">DWIGHT'S REVENGE</h1>
  <p class="abs front-question">Why would Dwight Kessler<br>align himself with<br>Gordon Pruett?</p>
  <p class="abs front-story">Dwight approached elected officials that he wanted to run for office, but did not have money to finance his campaign. He wanted other elected officials to finance his campaign. Everyone told him that they would help him get the vote out, but that he needed to finance his own race.</p>

  <div class="abs right-block intro-heading">
    <p class="kicker">IN COMES</p>
    <p class="kicker-name">GORDON PRUETT.</p>
  </div>
  <p class="abs right-block intro-text">Gordon Pruett who has a pay to play scheme over at the City, told Dwight he would finance his campaign on one condition.</p>
  <div class="abs right-block condition-heading">
    <p class="kicker">HE NEEDED TO RUN</p>
    <p class="kicker-name">AGAINST STEVEN HULSE.</p>
  </div>
  <p class="abs right-block closing-question">Why would Dwight want to run with no money?</p>
</section>

<section class="card card--back">
  <svg class="shapes" viewBox="0 0 790 553" width="790" height="553">
    <defs>
      <linearGradient id="mug-tone" x1="0" y1="0" x2="0" y2="1">
        <stop offset="0" stop-color="#f2f2f2"/>
        <stop offset="0.55" stop-color="#b59a88"/>
        <stop offset="1" stop-color="#1f3a2c"/>
      </linearGradient>
    </defs>
    <polygon fill="url(#mug-tone)" stroke="var(--red)" stroke-width="2.5" role="img" aria-label="Booking photo, profile facing left" points="334,153 360,108 415,108 441,153 415,199 360,199"/>
    <polygon fill="url(#mug-tone)" stroke="var(--red)" stroke-width="2.5" role="img" aria-label="Booking photo, profile facing right" points="334,297 360,252 415,252 441,297 415,343 360,343"/>
    <polygon fill="url(#mug-tone)" stroke="var(--red)" stroke-width="2.5" role="img" aria-label="Booking photo, full face" points="334,452 360,407 415,407 441,452 415,498 360,498"/>
    <rect x="455" y="364" width="98" height="129" fill="var(--paper)" stroke="var(--red)" stroke-width="1.5" role="img" aria-label="Criminal complaint one showing charges"/>
    <rect x="496" y="415" width="90" height="118" fill="var(--paper)" stroke="var(--red)" stroke-width="1.5" role="img" aria-label="Criminal complaint two showing charges"/>
  </svg>

  <h2 class="abs back-title"><span class="accent">DOMESTIC</span> VIOLENCE</h2>
  <p class="abs back-text back-text--reason">Dwight decided to run because no one on the school board would terminate Dwight's ex and her new boyfriend who both work for the school district. His ex even filed criminal charges against him that are still pending.</p>
  <p class="abs back-text back-text--goal">Dwight's ultimate goal is to terminate his ex and her new boyfriend if elected.</p>
  <p class="abs back-text back-text--majority">Plus Gordon Pruett needs the majority on the school board to do what he does bet.</p>
  <p class="abs kickbacks"><span class="accent">Kickbacks</span> for Contracts.</p>
  <p class="abs back-text back-text--contractors">They will hire their own contractors!</p>
  <p class="abs slogan"><span class="accent">Say "No" to Dwight's Revenge</span><br>and Gordon Pruett Money Grab!</p>

  <p class="abs charge charge--trespass">Criminal<br><span class="accent">TRESPASS</span></p>
  <p class="abs charge charge--mischief">Criminal<br><span class="accent">MISCHIEF</span></p>

  <div class="abs stamp-box"></div>
  <div class="abs address-line" style="top:177px"></div>
  <div class="abs address-line" style="top:213px"></div>
  <div class="abs address-line" style="top:250px"></div>
  <div class="abs address-line" style="top:286px"></div>
  <div class="abs address-line" style="top:323px"></div>
</section>

</body>
</html>
```